Web Site Design for a High End Travel Agency
Silverline Voyage Partners
This site is for a high end, travel service/concierge. Client's current site is located at www.silverlinevoyagepartners.net - Very old site.
I will repost this brief as a word doc also for clarification.
This new site needs to be similar to http://pravio.com/concierge.php or http://www.halvorsenmott.com. They want a dark background, very deep, rich colors (hunter greens, maybe dark blue, some gold). They also like the idea of a masthead that will change photos like the http://pravio.com/concierge.php and http://www.halvorsenmott.com site. We'll take care of that, however. Use the photo that we will attach to the project for the masthead.
The client does not have a logo, so use a very Rich, sharp font for their company name in the header.
For navigation, use:
* Home
* About (drop down)
* Services
* Destinations (drop down)
* Events (drop down)
* Request Quote
For body copy, use:
The Silverline Voyage Partners Advantage
Awarded one of the top travel companies of its kind, Silverline Voyage Partners treats all clients like VIPs. Elsa Rundqvist founded the company 10 years ago with the belief, "Our clients work hard for their money and deserve to get the best service along with the best value out there."
A few examples of our unique 1st class services:
* Customized travel arrangements
* Group travel presentations
* Customized Concierge Services
* Gift given when you receive your vacation documents
* Hand delivered travel brochures & documents to local clients
* Special contact number given just in case assistance is needed while traveling
Other home page sections:
FEATURED DESTINATIONS
(create 3 cells on the page, maybe side by side. One for the Caribbean, one for Europe, and one for Mexico) - Get the text that goes with each section from their current web site sidebar. You'll see the various cities/destinations listed in these sections. Use the photos attached to the brief for these sections.
Other sidebar items/sections:
Speak with a Destination Specialist
M-F 8 a.m.-7 p.m., Sat 9 a.m.-1 p.m. EST
FIND YOUR PERFECT GETAWAY (quote form)
Name
Phone
Email
Destination (drop down -put Europe first on list)
On footer, put:
* navigation menu:
Home I Site Map I Contact
* Copyright Statement:
Copyright Silverline Voyage Partners. All Rights Reserved
* Our link:
Web Site Design and Hosting by PixelForge Studios
* Facebook and Twitter Icons - Maybe a small square one for each
Travel
High end travel clientele and hotels purchase their services.
This will be a wordpress site. So, keep the design clean and professional. No tropical theme. This is high end, classy, elite.
Source Creative Brief. Please read this. It's the same as the brindlebox creative, but it's formatted better and easier to read.
main photo for masthead
mexico destination photo
Europe destination photo
caribbean destination photo

```html
<!DOCTYPE html>
<html lang="en">
<head>
<meta charset="utf-8">
<title>Silverline Voyage Partners</title>
<link rel="stylesheet" href="https://fonts.googleapis.com/css2?family=Arimo:ital,wght@0,400;0,700;1,400;1,700&display=swap">
<style>
:root{
  --bg-deep:#0b3a27;
  --bg-mid:#145a3d;
  --bg-stripe:#0e4630;
  --gold:#f2b51c;
  --gold-dark:#d18f06;
  --green:#5c8e12;
  --green-text:#4f8a10;
  --ink:#333333;
  --muted:#777777;
  --line:#d6d6d6;
  --panel:#ffffff;
  --nav:#ececec;
  --dark:#2b2b2b;
}
*{box-sizing:border-box;margin:0;padding:0}
html,body{width:1200px;height:1091px;overflow:hidden}
body{
  font-family:"Arimo",Arial,sans-serif;color:var(--ink);position:relative;
  background:
    radial-gradient(ellipse 520px 700px at 50% 45%,rgba(40,120,85,.55),transparent 75%),
    repeating-linear-gradient(90deg,var(--bg-deep) 0 22px,var(--bg-stripe) 22px 26px,var(--bg-mid) 26px 40px,var(--bg-stripe) 40px 44px);
}
.brand{position:absolute;top:70px;left:0;width:1200px;text-align:center;display:flex;justify-content:center;align-items:center;gap:12px}
.brand-dot{width:22px;height:22px;border-radius:50%;background:var(--gold)}
.brand-name{font-size:26px;font-weight:700;color:var(--gold);letter-spacing:1px}
.site{position:absolute;left:230px;top:163px;width:748px;height:895px;background:var(--panel);box-shadow:0 0 18px rgba(0,0,0,.55)}
.nav{position:absolute;left:0;top:0;width:748px;height:38px;background:linear-gradient(#f6f6f6,#dcdcdc);display:flex;border-bottom:1px solid #c8c8c8}
.nav a{font-size:11px;font-weight:700;color:#444;text-decoration:none;display:flex;align-items:center;padding:0 17px;border-right:1px solid #cfcfcf;height:38px;text-transform:uppercase}
.nav a.active{background:linear-gradient(#ffd54a,var(--gold-dark));color:#fff;padding:0 26px}
.nav .caret{font-size:8px;margin-left:4px}
.hero{position:absolute;left:12px;top:59px;width:722px;height:325px;background:linear-gradient(180deg,#6b5a3c 0%,#c89850 35%,#a06a30 60%,#4a3322 100%)}
.hero-arrow{position:absolute;top:142px;width:24px;height:40px;background:rgba(235,235,235,.9);display:flex;align-items:center;justify-content:center}
.hero-arrow.prev{left:-4px}.hero-arrow.next{right:-4px}
.caption{position:absolute;left:0;bottom:66px;width:722px;height:24px;background:rgba(20,20,20,.72);display:flex;align-items:center;padding-left:14px;font-size:11px;color:#fff}
.caption b{color:var(--gold);font-style:italic;margin-right:10px;letter-spacing:.5px}
.welcome{position:absolute;left:12px;top:404px;font-size:15px;font-style:italic;font-weight:700;color:var(--green-text)}
.intro{position:absolute;left:12px;top:428px;width:530px;font-size:9.5px;line-height:12px;color:#555}
.services-title{position:absolute;left:12px;top:476px;font-size:12.5px;font-style:italic;color:var(--green-text)}
.services{position:absolute;left:14px;top:497px;list-style:none}
.services li{font-size:9.5px;color:#555;height:14.5px;display:flex;align-items:center;gap:7px}
.specialist{position:absolute;left:346px;top:538px;font-size:11px;line-height:13px;color:#222}
.specialist h3{font-size:12.5px;font-style:italic;font-weight:700;color:var(--green-text);margin-bottom:3px}
.specialist .hl{color:var(--green);font-weight:700}
.specialist b{font-style:italic}
.quote{position:absolute;left:562px;top:419px;width:171px;height:193px;border:1px solid var(--line);background:#f7f7f7;padding:10px 9px}
.quote h4{font-size:11px;font-weight:400;color:#333;margin-bottom:8px}
.field{height:17px;border:1px solid #ccc;background:#fff;font-size:8.5px;color:#999;display:flex;align-items:center;padding-left:5px;margin-bottom:7px;justify-content:space-between;padding-right:5px}
.buttons{display:flex;gap:6px;margin-top:3px}
.btn{font-size:9px;height:16px;padding:0 9px;display:flex;align-items:center;color:#fff}
.btn.submit{background:var(--dark)}.btn.clear{background:var(--gold-dark)}
.featured{position:absolute;left:12px;top:637px;width:722px;height:232px;border:1px solid var(--line)}
.featured h2{font-size:11px;font-weight:400;color:#444;padding:10px 12px;border-bottom:1px solid var(--line);letter-spacing:.3px}
.dest{position:absolute;top:42px;width:222px}
.dest .photo{height:143px;border:3px solid #eee}
.dest p{text-align:center;font-size:12px;color:#333;margin-top:16px;letter-spacing:.5px}
.footer{position:absolute;left:12px;top:872px;width:722px;height:23px;display:flex;justify-content:space-between;align-items:center}
.footer-left{font-size:8px;color:#666;line-height:10px}
.follow{display:flex;align-items:center;gap:4px;font-size:11px;color:#444}
.follow span{margin-right:4px}
.sq{width:15px;height:15px;border-radius:2px}
</style>
</head>
<body>
<header class="brand"><span class="brand-dot"></span><span class="brand-name">SILVERLINE VOYAGE PARTNERS</span></header>
<div class="site">
  <nav class="nav">
    <a class="active">Home</a>
    <a>About Us<span class="caret">▼</span></a>
    <a>Services</a>
    <a>Destinations<span class="caret">▼</span></a>
    <a>Events<span class="caret">▼</span></a>
    <a>Request Quote</a>
    <a>Contact</a>
  </nav>
  <div class="hero" role="img" aria-label="Masthead photo: sunset view over a historic European city skyline">
    <div class="hero-arrow prev"><svg width="10" height="14"><path d="M8 1 2 7l6 6" fill="none" stroke="#555" stroke-width="2"/></svg></div>
    <div class="hero-arrow next"><svg width="10" height="14"><path d="M2 1l6 6-6 6" fill="none" stroke="#555" stroke-width="2"/></svg></div>
    <div class="caption"><b>SILVERLINE VOYAGE PARTNERS</b>| Speak with a Destination Specialist M-F 9 a.m.-7 p.m., Sat 9 a.m.-1 p.m. EST</div>
  </div>
  <h1 class="welcome">Welcome to Silverline Voyage Partners</h1>
  <p class="intro">Awarded one of the top travel companies of its kind, Silverline Voyage Partners treats all clients like VIPs. Elsa Rundqvist founded the company 10 years ago with the belief, "Our clients work hard for their money and deserve to get the best service along with the best value out there."</p>
  <h2 class="services-title">A few examples of our unique 1st class services:</h2>
  <ul class="services">
    <li><svg width="7" height="8"><path d="M0 0l7 4-7 4z" fill="#555"/></svg>Customized travel arrangements</li>
    <li><svg width="7" height="8"><path d="M0 0l7 4-7 4z" fill="#555"/></svg>Group travel presentations</li>
    <li><svg width="7" height="8"><path d="M0 0l7 4-7 4z" fill="#555"/></svg>Customized Concierge Services</li>
    <li><svg width="7" height="8"><path d="M0 0l7 4-7 4z" fill="#555"/></svg>Gift given when you receive your vacation documents</li>
    <li><svg width="7" height="8"><path d="M0 0l7 4-7 4z" fill="#555"/></svg>Hand delivered travel brochures &amp; documents to local clients</li>
    <li><svg width="7" height="8"><path d="M0 0l7 4-7 4z" fill="#555"/></svg>Special contact number given just in case assistance is needed</li>
    <li style="padding-left:14px">while traveling</li>
  </ul>
  <div class="specialist">
    <h3>Speak with Our Specialist</h3>
    <b>410.555.0142</b><br>
    <b>Monday-Friday</b> <span class="hl">9 a.m.-7 p.m.</span><br>
    <b>Saturday</b> <span class="hl">9 a.m.-1 p.m. EST</span>
  </div>
  <form class="quote">
    <h4>Find your Perfect Getaway</h4>
    <div class="field">Name</div>
    <div class="field">Phone</div>
    <div class="field">Email Address</div>
    <div class="field">Europe<svg width="8" height="5"><path d="M0 0h8L4 5z" fill="#777"/></svg></div>
    <div class="buttons"><span class="btn submit">Submit</span><span class="btn clear">Clear</span></div>
  </form>
  <section class="featured">
    <h2>FEATURED DESTINATIONS</h2>
    <div class="dest" style="left:12px"><div class="photo" role="img" aria-label="Caribbean beach with turquoise water and palm trees" style="background:linear-gradient(180deg,#bfe3f5 0%,#5fc2d6 45%,#2fa3b4 65%,#e7dcc0 100%)"></div><p>THE CARIBBEAN</p></div>
    <div class="dest" style="left:250px"><div class="photo" role="img" aria-label="European city landmark lit up at night" style="background:linear-gradient(180deg,#1a1a2a 0%,#3a2f2a 45%,#b68a3a 75%,#2a2320 100%)"></div><p>THE EUROPE</p></div>
    <div class="dest" style="left:488px"><div class="photo" role="img" aria-label="Mexican coastal bay with hotels and blue sea" style="background:linear-gradient(180deg,#8fc4ea 0%,#cfe6f4 35%,#2d7fb8 60%,#1d5f95 100%)"></div><p>THE MEXICO</p></div>
  </section>
  <footer class="footer">
    <div class="footer-left">Home &nbsp;|&nbsp; Site Map &nbsp;|&nbsp; Contact<br>© 2013 Silverline Voyage Partners. All Rights Reserved.</div>
    <div class="follow"><span>Follow Us:</span>
      <i class="sq" style="background:#3b5998"></i><i class="sq" style="background:#2aa9e0"></i><i class="sq" style="background:#3d7bc4"></i><i class="sq" style="background:#2a6ea8"></i><i class="sq" style="background:#d23c2a"></i><i class="sq" style="background:#e47b1c"></i>
    </div>
  </footer>
</div>
</body>
</html>
```